Flock and co fleece works pty ltd

We are sheep shearing contractors,we are looking for a simple design business card, with a drawing like picture of a Australian sheep on it, then just standard details, name, phone, email, po box.
We would like double sided, with 2 lines of wiriting on the back, no bright colours please.
We like black and white, doesn't have to be too serious, however nothing to far left of cwntre.
On the back of the card we would like professional shearing contract offering full contract team.
Can use use the symbol & in the name instead of and.

Target Market(s)

Sheep farmers, target males from age 20 and up

Contact Information for Business Card

Company name flock and co fleece works pty ltd
Darren holloway 0491352706, po box 4071 sale vic 3853,
Email flockandcofleece@mailbarn.example, gippsland shearing contractor

Font styles to use
Serif

Colors

Designer to choose only greyscale colors for use in the design.

Requirements
Nice to have
• Simple design

```html
<!DOCTYPE html>
<html lang="en">
<head>
<meta charset="utf-8">
<title>Flock and co fleece works – business card</title>
<link rel="stylesheet" href="https://fonts.googleapis.com/css2?family=Lora:wght@400;700&display=swap">
<style>
  :root {
    --page: #2b2b2b;
    --card: #ffffff;
    --ink: #111111;
    --ink-soft: #2a2a2a;
    --rule: #6e6e6e;
    --art-dark: #1a1a1a;
    --art-mid: #4a4a4a;
    --art-faint-a: #ececec;
    --art-faint-b: #f5f5f5;
  }
  * { box-sizing: border-box; margin: 0; padding: 0; }
  html, body {
    width: 1200px; height: 1200px; overflow: hidden;
    background: var(--page);
    font-family: "Lora", Georgia, serif;
    color: var(--ink);
  }
  .card {
    position: absolute; left: 150px;
    width: 900px; height: 514px;
    background: var(--card);
    box-shadow: 0 10px 30px rgba(0,0,0,.45);
    overflow: hidden;
  }
  .card--back { top: 56px; }
  .card--front { top: 630px; }

  /* back */
  .back-art {
    position: absolute; left: 330px; top: 70px;
    width: 430px; height: 420px;
    background: radial-gradient(ellipse at 55% 50%, var(--art-faint-a), var(--art-faint-b) 70%, transparent 72%);
  }
  .write-line {
    position: absolute; left: 140px; right: 36px;
    height: 1px; background: var(--rule);
  }
  .write-line:nth-of-type(2) { top: 180px; }
  .write-line:nth-of-type(3) { top: 242px; }
  .write-line:nth-of-type(4) { top: 304px; }
  .back-name {
    position: absolute; left: 330px; top: 372px;
  }

  /* shared wordmark */
  .wordmark { font-weight: 700; color: var(--ink); line-height: 1; }
  .wordmark__main { display: block; font-size: 50px; }
  .wordmark__sub { display: block; font-size: 22px; margin-top: 6px; letter-spacing: .3px; }

  /* front */
  .front-art {
    position: absolute; left: 40px; top: 50px;
    width: 350px; height: 420px;
    background: radial-gradient(ellipse at 50% 50%, var(--art-mid), var(--art-dark) 60%, transparent 62%);
  }
  .front-info {
    position: absolute; left: 450px; top: 108px; right: 30px;
  }
  .person { margin-top: 40px; }
  .person__name { font-size: 36px; font-weight: 700; line-height: 1.1; }
  .person__role { font-size: 24px; font-weight: 400; color: var(--ink-soft); margin-top: 2px; }
  .contacts { list-style: none; margin-top: 30px; }
  .contacts li {
    display: flex; align-items: center; gap: 14px;
    font-size: 23px; line-height: 1.35; color: var(--ink-soft);
  }
  .contacts svg { width: 18px; height: 18px; flex: none; fill: var(--ink); }
</style>
</head>
<body>

<section class="card card--back" aria-label="Card back">
  <div class="back-art" role="img" aria-label="Faint illustration of a shearer in a hat shearing a sheep"></div>
  <div class="write-line"></div>
  <div class="write-line"></div>
  <div class="write-line"></div>
  <div class="back-name wordmark">
    <span class="wordmark__main">Flock and co</span>
    <span class="wordmark__sub">fleece works pty ltd</span>
  </div>
</section>

<section class="card card--front" aria-label="Card front">
  <div class="front-art" role="img" aria-label="Black and white illustration of a shearer in a hat shearing a sheep"></div>
  <div class="front-info">
    <div class="wordmark">
      <span class="wordmark__main">Flock and co</span>
      <span class="wordmark__sub">fleece works pty ltd</span>
    </div>
    <div class="person">
      <p class="person__name">Darren holloway</p>
      <p class="person__role">Gippsland shearing contractor</p>
    </div>
    <ul class="contacts">
      <li>
        <svg viewBox="0 0 24 24" aria-hidden="true"><path d="M6.6 10.8a15.2 15.2 0 0 0 6.6 6.6l2.2-2.2a1 1 0 0 1 1-.25 11.4 11.4 0 0 0 3.6.57 1 1 0 0 1 1 1V20a1 1 0 0 1-1 1A17 17 0 0 1 3 4a1 1 0 0 1 1-1h3.5a1 1 0 0 1 1 1c0 1.25.2 2.45.57 3.6a1 1 0 0 1-.25 1z"/></svg>
        <span>0491352706</span>
      </li>
      <li>
        <svg viewBox="0 0 24 24" aria-hidden="true"><path d="M12 2a7 7 0 0 0-7 7c0 5.2 7 13 7 13s7-7.8 7-13a7 7 0 0 0-7-7zm0 9.5A2.5 2.5 0 1 1 12 6.5a2.5 2.5 0 0 1 0 5z"/></svg>
        <span>Po box 4071 sale vic 3853,</span>
      </li>
      <li>
        <svg viewBox="0 0 24 24" aria-hidden="true"><path d="M2 5h20v14H2zm2 2v.5l8 5.5 8-5.5V7zm0 2.9V17h16V9.9l-8 5.5z"/></svg>
        <span>flockandcofleece@mailbarn.example</span>
      </li>
    </ul>
  </div>
</section>

</body>
</html>
```